LoftGroove365 - Internet Radio Station Needs a Website

Site Description:
Loftgroove365 is an Internet radio station feed that broadcasts House music 24 hours per day, 7 days per week. The stream is hosted by Trelbay.example, a WaveLoom partner. Loftgroove365 has various programming schedules and an Auto DJ program is enabled when there is no live programming. There are several DJs that provide content for programming, and Loftgroove365 also does live pop-up events at various venues. Currently, there is no front-end design, if you visit loftgroove365.example or loftgroove365.example.com, each domain URL is pointed to the default WaveLoom player and feed that is hosted by Trelbay. The goal is to create a front-end design and website that will be optimized for mobile devices, as most of the streaming will be to mobile devices; the site should be responsive.

Here are some templates that offer similar functionality:
https://www.pagekiln.example/demo/40317.html
https://www.pagekiln.example/demo/46820.html

LOGO and Aesthetics:
From an aesthetic standpoint, house music is a very underground, New York-centric genre of music. I have uploaded an image that mirrors the Dorvale Underline signage motif. I like the underground feel and "grittyness" of the subway. I want to make sure that the "2", "4", and "7" images in their respective circles and colors (red, green, and purple) are utilized in any logo design, these subway lines are highly recognizable and I want to play off that familiarity because everyone in New York City can identify with them (the fonts and colors would need to remain as depicted in the attachment). I need a logo that can fit into a square (or circle) so that it can be used for social media profiles; I am not opposed to the abbreviation "LG365" or some configuration whereby the "House Music" is above the (larger) "2 4 7". I have also included a picture of an electronic board that New York trains have which shows upcoming stops; possibly a navigation bar or site template might follow a similar motif.

Site Requirements:

- Text Message (SMS) API integration. I do plan on developing a mobile app, complete with push notification capabilities; however, I’d like to know whether sending SMS messages is possible in the interim, even if a subscription to a third-party service is required.

- Social Media Integration. At a minimum, users should be able to connect via Chirpnest, Quillo, and Snapvane. I’d like to be able to incorporate the Chirpnest Live capabilities if a Chirpnest page is integrated.

- Content Management System (CMS). I need to be able to update content easily, particularly the Events calendar, Schedule, and Archives (regularly upload mp3 files/podcasts). Perhaps this means that the site needs to be a PageForge site.

- LIVE Button. I would like to “activate” a LIVE button and possible scrolling message or other text (on the Home Page) to correspond to live shows and events.

Site Design:
Initially, there will be six (6) pages/sections, based on the following site navigation buttons:

HOME / DJs & SHOWS / SCHEDULE / EVENTS / BLOG / IN THE MIX

- HOME: the landing page would enable anyone, registered or not, to simply click on the listen button and tune in. There would also be featured charts and playlists that would change from week to week. Users would be given the option to register and sign-in for the “premium” experience (subscribing to shows, viewing song info, access to the archives for an offline experience). All social media integration would appear on the Home Page (and probably every other page as well)

- DJs & SHOWS: DJ bios and show descriptions would be provided, along with contact information and social media links for individual DJs. Downloadable press kits for each DJ would be available here, and a “Book Me” (contact form) email form as well.

- SCHEDULE: this would be a calendar showing daily programming and upcoming shows (by month)

- EVENTS: this would show upcoming events, complete with any flyer artwork and Roamly Maps integration (API). Maybe even Chirpnest event integration (who’s going, etc)

- BLOG: blog section complete with the ability to upload videos, audio, and images to associate with the written content

- IN THE MIX: this section will have archives of DJ mixes and shows, for offline listening. Registered users would have access to this section so that they can download any of the archived mixes for offline listening. The mixes would be indexed but should also be searchable by DJ or keyword.

Target Market(s)

18-40, people who frequently go out to bars, clubs, lounges

Industry/Entity Type

Radio Station

Logo Text

"Loft Groove 365" or "LG365"

Coding

Coded - Design and coding required

Font styles to use
Sans Serif

Requirements
Must have
• - Optimized for mobile (Responsive)
• - Pull stream from Trelbay/WaveLoom server, a “LISTEN NOW” button should prominently appear on the Home page. Once a listener clicks on the button, the audio should stream on the same page (without a new page having to be opened). If a listener wishes to navigate throughout the site, a pop-up window should appear with the player controls. There are various WaveLoom-compatible players that can be embedded in the site, or there should be a way to link a button to the actual stream destination (http://s1.trelbay.example:8808/index.html OR http://station.trelbay.example/a93c1e0d27fb4/)
• - Sign In/Register option. Non-registered users can listen, but will not have access to all areas of the site. Once signed in, a user would have access to all areas of the site (including archived mixes/podcasts). Registration would require a name, email address, possible Chirpnest sign-in, and a mobile device number (optional). Signed in users would be able to ‘Like’, ‘Share’, ‘Tweet’, etc. and possibly even create their own playlists.
Nice to have
• - Text Message (SMS) API integration. I do plan on developing a mobile app, complete with push notification capabilities; however, I’d like to know whether sending SMS messages is possible in the interim, even if a subscription to a third-party service is required.
• - LIVE Button. I would like to “activate” a LIVE button and possible scrolling message or other text (on the Home Page) to correspond to live shows and events.

```html
<!DOCTYPE html>
<html lang="en">
<head>
<meta charset="utf-8">
<title>Loft Groove 365 — Internet Radio Station</title>
<link href="https://fonts.googleapis.com/css2?family=Montserrat:wght@400;500;600;700&family=Open+Sans:wght@400;600&display=swap" rel="stylesheet">
<style>
:root{
  --red:#e8202a;
  --green:#14934a;
  --purple:#c4489c;
  --ink:#1f1f1f;
  --text:#8a8a8a;
  --grey-band:#f3f3f3;
  --footer:#2b2b2b;
  --white:#ffffff;
}
*{margin:0;padding:0;box-sizing:border-box}
html,body{width:1200px;height:2459px;overflow:hidden}
body{position:relative;background:var(--white);font-family:"Open Sans",Arial,sans-serif;color:var(--ink)}
.abs{position:absolute}
.heading{font-family:"Montserrat",Arial,sans-serif;font-weight:500;color:var(--ink);text-transform:uppercase}

/* Hero */
.hero{left:0;top:0;width:1200px;height:560px;overflow:hidden}
.hero-photo{position:absolute;inset:0;background:
  radial-gradient(ellipse at 62% 30%,rgba(180,120,150,.55),transparent 45%),
  radial-gradient(ellipse at 80% 70%,rgba(120,40,150,.7),transparent 55%),
  linear-gradient(100deg,#0f2c3c 0%,#3a2a55 40%,#6b2a7a 70%,#3b1850 100%)}
.brand{left:133px;top:30px;display:flex;flex-direction:column;gap:6px;border-top:2px solid var(--white);padding-top:7px;width:210px}
.brand-name{display:flex;align-items:center;gap:8px;font-family:"Montserrat",sans-serif;font-weight:600;font-size:17px;color:var(--white)}
.brand-dot{width:14px;height:14px;border-radius:50%;background:var(--red)}
.brand-url{font-size:8px;color:rgba(255,255,255,.75);text-align:right}
.nav{left:0;top:0;width:1200px}
.nav a{position:absolute;top:58px;font-family:"Montserrat",sans-serif;font-weight:600;font-size:11px;color:var(--white);text-decoration:none;text-transform:uppercase;white-space:nowrap}
.nav .active{left:577px;top:40px;width:52px;height:52px;border-radius:50%;background:var(--red);display:flex;align-items:center;justify-content:center}
.listen-top{left:947px;top:0;width:120px;height:38px;background:var(--green);color:var(--white);display:flex;align-items:center;justify-content:center;gap:8px;font-family:"Montserrat",sans-serif;font-weight:600;font-size:13px}
.hero-title{left:131px;top:195px;font-family:"Montserrat",sans-serif;font-weight:500;font-size:39px;color:var(--white);letter-spacing:.5px}
.hero-sub{left:133px;top:255px;font-family:"Montserrat",sans-serif;font-size:19px;line-height:27px;color:var(--white);text-transform:uppercase}
.listen-btn{left:131px;top:341px;width:185px;height:53px;background:var(--red);color:var(--white);display:flex;align-items:center;justify-content:center;gap:10px;font-family:"Montserrat",sans-serif;font-weight:500;font-size:19px}
.account{left:134px;top:416px;font-family:"Montserrat",sans-serif;font-weight:600;font-size:11px;color:var(--white);word-spacing:2px}
.account span{margin:0 18px}
.slide-arrow{top:288px;width:46px;height:45px;background:rgba(0,0,0,.55);display:flex;align-items:center;justify-content:center}

/* Featured charts */
.section-title{font-size:28px}
.chart-card{top:690px;width:279px;height:346px;overflow:hidden}
.chart-name{position:absolute;left:23px;top:135px;font-family:"Montserrat",sans-serif;font-weight:500;font-size:36px;line-height:47px;color:var(--white);text-transform:uppercase}
.chart-date{position:absolute;left:21px;top:253px;width:73px;height:73px;border-radius:50%;display:flex;align-items:center;justify-content:center;font-family:"Montserrat",sans-serif;font-size:19px;color:var(--white)}

/* Services */
.band{left:0;top:1124px;width:1200px;height:636px;background:var(--grey-band)}
.service{top:1183px;width:279px;height:497px;background:var(--white);border-top:6px solid;text-align:center}
.service-icon{position:absolute;left:73px;top:46px;width:133px;height:133px;border-radius:50%;display:flex;align-items:center;justify-content:center}
.service-title{position:absolute;left:0;top:212px;width:100%;font-size:28px}
.service-text{position:absolute;left:24px;top:272px;width:231px;font-size:11.5px;line-height:24px;color:var(--text)}
.btn-dark{background:var(--ink);color:var(--white);font-family:"Montserrat",sans-serif;font-weight:600;font-size:11px;display:flex;align-items:center;justify-content:center;text-transform:uppercase}
.service .btn-dark{position:absolute;left:74px;top:373px;width:131px;height:48px}

/* News & chart */
.news-thumb{top:1903px;width:145px;height:121px}
.news-title{top:1900px;font-size:19px}
.news-text{top:1930px;width:140px;font-size:11px;line-height:24px;color:var(--text)}
.playlist{left:818px;top:1895px;list-style:none}
.playlist li{display:flex;align-items:center;gap:14px;height:36.7px;font-size:12.5px;color:#555;white-space:nowrap}
.playlist svg{flex:none}

/* Footer */
.footer{left:0;top:2168px;width:1200px;height:228px;background:var(--footer);color:var(--white)}
.footer h4{position:absolute;top:40px;font-family:"Montserrat",sans-serif;font-weight:500;font-size:15px;text-transform:uppercase}
.contact-list{position:absolute;left:413px;top:80px;list-style:none;font-size:10.5px}
.contact-list li{display:flex;gap:14px;align-items:flex-start;height:26px}
.newsletter-text{position:absolute;left:639px;top:78px;width:215px;font-size:11px;line-height:19px}
.email-field{position:absolute;left:639px;top:128px;width:213px;height:32px;background:var(--white);color:#777;font-size:10.5px;padding:9px 14px}
.subscribe{position:absolute;left:639px;top:170px;width:76px;height:20px;background:var(--green);font-family:"Montserrat",sans-serif;font-size:9px;font-weight:600;display:flex;align-items:center;justify-content:center}
.follow-text{position:absolute;left:898px;top:82px;width:180px;font-size:11px;line-height:18px}
.social{position:absolute;top:147px;width:33px;height:33px;border-radius:50%;border:1.5px solid var(--white)}
.copyright{left:0;top:2396px;width:1200px;height:63px;background:var(--red);color:var(--white);font-size:11px;display:flex;align-items:center;justify-content:center}
</style>
</head>
<body>

<header class="abs hero">
  <div class="hero-photo" role="img" aria-label="Photo of a DJ mixing on decks in a smoky purple-lit club"></div>

  <div class="abs brand">
    <div class="brand-name"><span>Loft Groove 365</span><span class="brand-dot"></span></div>
    <div class="brand-url">www.loftgroove365.example</div>
  </div>

  <nav class="abs nav">
    <a class="active" href="#">Home</a>
    <a style="left:654px" href="#">DJs &amp; Shows</a>
    <a style="left:766px" href="#">Schedule</a>
    <a style="left:860px" href="#">Events</a>
    <a style="left:938px" href="#">Blog</a>
    <a style="left:1004px" href="#">In the Mix</a>
  </nav>

  <div class="abs listen-top">
    <svg width="18" height="14" viewBox="0 0 18 14"><path d="M1 4h3l4-3v12l-4-3H1z" fill="#fff"/><path d="M11 4q2 3 0 6M13.5 2q4 5 0 10" stroke="#fff" stroke-width="1.5" fill="none"/></svg>
    LISTEN
  </div>

  <h1 class="abs hero-title">INTERNET RADIO STATION</h1>
  <p class="abs hero-sub">Broadcasts house music 24 hours per day,<br>7 days per week.</p>

  <div class="abs listen-btn">
    <svg width="18" height="16" viewBox="0 0 18 16"><path d="M2 10V8a7 7 0 0 1 14 0v2" stroke="#fff" stroke-width="2" fill="none"/><rect x="1" y="9" width="4" height="6" rx="1" fill="#fff"/><rect x="13" y="9" width="4" height="6" rx="1" fill="#fff"/></svg>
    LISTEN
  </div>
  <div class="abs account">SIGN IN<span style="font-weight:400">|</span>REGISTER</div>

  <div class="abs slide-arrow" style="left:0"><svg width="10" height="16" viewBox="0 0 10 16"><path d="M8 2 2 8l6 6" stroke="#fff" stroke-width="1.6" fill="none"/></svg></div>
  <div class="abs slide-arrow" style="left:1154px"><svg width="10" height="16" viewBox="0 0 10 16"><path d="M2 2l6 6-6 6" stroke="#fff" stroke-width="1.6" fill="none"/></svg></div>
</header>

<section>
  <h2 class="abs heading section-title" style="left:133px;top:610px">Featured Charts</h2>
  <svg class="abs" style="left:1012px;top:614px" width="52" height="30" viewBox="0 0 52 30"><path d="M20 3 8 15l12 12" stroke="#1f1f1f" stroke-width="5" fill="none"/><path d="M32 3l12 12-12 12" stroke="#1f1f1f" stroke-width="5" fill="none"/></svg>

  <article class="abs chart-card" style="left:133px;background:linear-gradient(160deg,#2b3a66,#121a33 60%,#0a0f22)" role="img" aria-label="Concert photo of a guitarist on a blue-lit stage">
    <div class="chart-name">Theo<br>Marrick</div>
    <div class="chart-date" style="background:var(--red)">23/12</div>
  </article>
  <article class="abs chart-card" style="left:460px;background:linear-gradient(160deg,#4a4038,#7a6a58 50%,#2a2420)" role="img" aria-label="Photo of a DJ in a hooded top and sunglasses">
    <div class="chart-name">Copper<br>Veil</div>
    <div class="chart-date" style="background:var(--green)">23/12</div>
  </article>
  <article class="abs chart-card" style="left:788px;background:linear-gradient(150deg,#e29a7a,#b44a9a 45%,#5a1f6a)" role="img" aria-label="Photo of a performer playing guitar in pink stage light">
    <div class="chart-name">Ivo<br>Brandt</div>
    <div class="chart-date" style="background:var(--purple)">23/12</div>
  </article>
</section>

<section class="abs band"></section>

<article class="abs service" style="left:133px;border-color:var(--red)">
  <div class="service-icon" style="background:var(--red)"><svg width="26" height="36" viewBox="0 0 26 36"><rect x="8" y="2" width="10" height="19" rx="5" fill="#fff"/><path d="M4 15a9 9 0 0 0 18 0M13 24v8M8 33h10" stroke="#fff" stroke-width="2.2" fill="none"/></svg></div>
  <h3 class="heading service-title">DJs &amp; Shows</h3>
  <p class="service-text">Mes cuml dia sed in lacus ut eniascet ingerto alliqt es site amet eismod ictor ut ligulate ameti dapibus t</p>
  <div class="btn-dark">Learn More</div>
</article>
<article class="abs service" style="left:460px;border-color:var(--green)">
  <div class="service-icon" style="background:var(--green)"><svg width="34" height="34" viewBox="0 0 34 34"><rect x="2" y="5" width="30" height="27" rx="2" fill="#fff"/><rect x="8" y="1" width="3" height="8" fill="#fff"/><rect x="23" y="1" width="3" height="8" fill="#fff"/><g fill="#14934a"><rect x="6" y="13" width="5" height="4"/><rect x="14" y="13" width="5" height="4"/><rect x="22" y="13" width="5" height="4"/><rect x="6" y="20" width="5" height="4"/><rect x="14" y="20" width="5" height="4"/><rect x="22" y="20" width="5" height="4"/><rect x="6" y="27" width="5" height="3"/><rect x="14" y="27" width="5" height="3"/></g></svg></div>
  <h3 class="heading service-title">Schedule</h3>
  <p class="service-text">Mes cuml dia sed in lacus ut eniascet ingerto alliqt es site amet eismod ictor ut ligulate ameti dapibus t</p>
  <div class="btn-dark">Learn More</div>
</article>
<article class="abs service" style="left:788px;border-color:var(--purple)">
  <div class="service-icon" style="background:var(--purple)"><svg width="34" height="38" viewBox="0 0 34 38"><path d="M2 2h30L17 20z" fill="#fff"/><path d="M17 19v14M9 35h16" stroke="#fff" stroke-width="3"/></svg></div>
  <h3 class="heading service-title">Events</h3>
  <p class="service-text">Mes cuml dia sed in lacus ut eniascet ingerto alliqt es site amet eismod ictor ut ligulate ameti dapibus t</p>
  <div class="btn-dark">Learn More</div>
</article>

<section>
  <h2 class="abs heading section-title" style="left:133px;top:1834px">Latest News</h2>
  <div class="abs news-thumb" style="left:133px;background:linear-gradient(140deg,#9fd6ea,#3b7fa6 50%,#0e2533)" role="img" aria-label="Photo of a stage microphone in front of a bright crowd"></div>
  <h3 class="abs heading news-title" style="left:297px">DJs &amp; Shows</h3>
  <p class="abs news-text" style="left:297px">Mes cuml dia sed in lacus ut eniascet ingerto alliqt es site amet eismod</p>
  <div class="abs news-thumb" style="left:454px;background:linear-gradient(140deg,#d23ca0,#6a2a8a 50%,#1a0f2a)" role="img" aria-label="Photo of DJ turntables under magenta light"></div>
  <h3 class="abs heading news-title" style="left:619px">DJs &amp; Shows</h3>
  <p class="abs news-text" style="left:619px">Mes cuml dia sed in lacus ut eniascet ingerto alliqt es site amet eismod</p>
  <div class="abs btn-dark" style="left:133px;top:2062px;width:115px;height:42px">View All</div>

  <h2 class="abs heading section-title" style="left:816px;top:1834px">Music Chart</h2>
  <ul class="abs playlist">
    <li><svg width="12" height="12" viewBox="0 0 12 12"><circle cx="6" cy="6" r="5" fill="none" stroke="#c4489c" stroke-width="1.5"/><path d="M4.5 3.5 8 6l-3.5 2.5z" fill="#c4489c"/></svg>Rolan Devere — Night Signal</li>
    <li><svg width="12" height="12" viewBox="0 0 12 12"><circle cx="6" cy="6" r="5" fill="none" stroke="#c4489c" stroke-width="1.5"/><path d="M4.5 3.5 8 6l-3.5 2.5z" fill="#c4489c"/></svg>Rolan Devere — Wandering Past Midnight</li>
    <li><svg width="12" height="12" viewBox="0 0 12 12"><circle cx="6" cy="6" r="5" fill="none" stroke="#c4489c" stroke-width="1.5"/><path d="M4.5 3.5 8 6l-3.5 2.5z" fill="#c4489c"/></svg>Wes Calloway — Harbor Rain</li>
    <li><svg width="12" height="12" viewBox="0 0 12 12"><circle cx="6" cy="6" r="5" fill="none" stroke="#c4489c" stroke-width="1.5"/><path d="M4.5 3.5 8 6l-3.5 2.5z" fill="#c4489c"/></svg>Harbor Lane — Another Summer</li>
    <li><svg width="12" height="12" viewBox="0 0 12 12"><circle cx="6" cy="6" r="5" fill="none" stroke="#c4489c" stroke-width="1.5"/><path d="M4.5 3.5 8 6l-3.5 2.5z" fill="#c4489c"/></svg>Wes Calloway — Glass and Gold</li>
    <li><svg width="12" height="12" viewBox="0 0 12 12"><circle cx="6" cy="6" r="5" fill="none" stroke="#c4489c" stroke-width="1.5"/><path d="M4.5 3.5 8 6l-3.5 2.5z" fill="#c4489c"/></svg>Otis Framwell — Dancing With The Tide</li>
  </ul>
</section>

<footer class="abs footer">
  <div class="brand" style="position:absolute;left:133px;top:40px;width:230px">
    <div class="brand-name" style="font-size:19px"><span>Loft Groove 365</span><span class="brand-dot" style="width:16px;height:16px"></span></div>
    <div class="brand-url">www.loftgroove365.example</div>
  </div>

  <h4 style="left:413px">Contact Us</h4>
  <ul class="contact-list">
    <li><svg width="12" height="12" viewBox="0 0 12 12"><path d="M1 4q5-4 10 0v2H8V4.5H4V6H1z M2 7h8v4H2z" fill="#fff"/></svg>(000)-121-1231 &nbsp;(Phone)</li>
    <li><svg width="12" height="12" viewBox="0 0 12 12"><rect x="3" y="1" width="6" height="3" fill="#fff"/><rect x="1" y="4" width="10" height="5" fill="#fff"/><rect x="3" y="8" width="6" height="3" fill="#fff"/></svg>(000)-121-1231 &nbsp;(Fax)</li>
    <li><svg width="12" height="12" viewBox="0 0 12 12"><rect x="1" y="2.5" width="10" height="7" fill="#fff"/><path d="M1 2.5l5 4 5-4" stroke="#2b2b2b" fill="none"/></svg><span style="text-decoration:underline">info@loftgroove365.example</span></li>
    <li><svg width="12" height="12" viewBox="0 0 12 12"><path d="M6 11S2 7 2 4.5a4 4 0 0 1 8 0C10 7 6 11 6 11z" fill="#fff"/><circle cx="6" cy="4.5" r="1.5" fill="#2b2b2b"/></svg><span style="line-height:14px"># 2564 Lorem Ipsum Dummy<br>Lorem Ipsum Dummy</span></li>
  </ul>

  <h4 style="left:639px">Newsletter</h4>
  <p class="newsletter-text">Register Your email address to get information about us</p>
  <div class="email-field">Email Address</div>
  <div class="subscribe">SUBSCRIBE</div>

  <h4 style="left:898px">Follow Us</h4>
  <p class="follow-text">Lorem ipsum dolor sit amet, conse ctetur adipiscing elit. Nulla in purus nibh. Donec ornare</p>
  <a class="social" style="left:896px" href="#" aria-label="Chirpnest"></a>
  <a class="social" style="left:934px" href="#" aria-label="Quillo"></a>
  <a class="social" style="left:974px" href="#" aria-label="Snapvane"></a>
</footer>

<div class="abs copyright">© Copyright 2017 Internet Radio.All Rights Reserved</div>

</body>
</html>
```